Wellness Coach/Personal trainer needs wordpress site/blog with ecommerce capable membership area

We need a WordPress design for PlumHarborFit.com. This is a blog about wellness, weight loss, and health related topics. Design logo will be provided to the winner.

A great site with a design that we would like to emulate are http://kq4.example. The design should be simple, clean, unique, fun, and distinctive. Above all, it should be highly readable and easy to navigate.

These are the specific sections/categories of the blog that should be included and incorporated into the design SEE BELOW.

Thanks in advance for your consideration
Updates

Reason: I have extended the deadline to evaluate more designs from other pros

Hello all, Please take a minute to review the requirements for this project and please make sure you are capable of meeting ALL the requirements. As you already know I will be making a decision very shortly on whose design I will be moving forward with, if there are any last minute submissions now is the time. Thank you for your time.

Target Market(s)

90 % women 10 % men my clients are usually professionals who value their appearance, health, longevity and time.

Industry/Entity Type

Personal Trainer

Font styles to use
Serif

Colors
886aae
ffcf3e

Requirements
Must have
• Requirements

- start losing weight today.... 555 902 6148 (first line)
- visuals/images and backgrounds to give the idea of wellness, weight loss, healthy living, etc
- navigation menu - home, who we are, what we do, who we serve, blog, contact, members area

1) slider element at top below navigation menu
2) slider element near bottom of page will have testimonials
3) contact form/inquiry form (one page)
4) will provide wellness logo (to give credibility)
5) color scheme purple, gold and white
6) membership area
7) fb, tw, youtube icons
8) footer area - In the footer, there will be smaller company logo, copyright,
disclaimer, privacy policy, terms n conditions, verse of day, and contact info, Phone: (555) 902-6148
Email: support@...
Address:
9) use dummy content/graphic as they will be replaced by real content (the winner will provide instruction on how to make changes to all text and changing graphics)
9) ecommerce enabled / newsletter signup area

```html
<!DOCTYPE html>
<html lang="en">
<head>
<meta charset="utf-8">
<title>Plum Harbor Fit</title>
<link rel="stylesheet" href="https://fonts.googleapis.com/css2?family=Questrial&family=Oswald:wght@400;500&family=Roboto+Condensed:wght@300;400&family=Roboto:wght@400&family=Lato:wght@300;400&family=Tinos:wght@700&display=swap">
<style>
:root{
  --brand:#886aae;
  --brand-dark:#6d5192;
  --ink:#333333;
  --charcoal:#343434;
  --paper:#efefef;
  --card:#ffffff;
  --text:#555555;
  --muted:#7a7a7a;
  --link:#6d5192;
  --gold:#ffcf3e;
  --base:#5a5a5a;
}
*{margin:0;padding:0;box-sizing:border-box}
html,body{width:964px;height:1200px;overflow:hidden}
body{position:relative;background:var(--paper);font-family:"Lato",sans-serif;color:var(--text)}
.abs{position:absolute}
.header{left:0;top:0;width:964px;height:117px;background:var(--brand)}
.brand{left:110px;top:32px;font-family:"Questrial",sans-serif;font-size:36px;color:#fff;letter-spacing:1px;white-space:nowrap}
.phone{right:88px;top:22px;font-family:"Roboto Condensed",sans-serif;font-size:19px;color:#fff}
.hours{right:88px;top:55px;text-align:right;font-family:"Roboto Condensed",sans-serif;font-size:8.5px;line-height:13px;color:#fff;white-space:nowrap}
.nav{left:0;top:117px;width:964px;height:40px;background:var(--charcoal)}
.nav a{position:absolute;top:15px;font-family:Arial,sans-serif;font-size:10px;color:#fff;text-decoration:none;white-space:nowrap}
.search{left:746px;top:7px;width:130px;height:27px;border:1px solid #555;background:#2e2e2e;color:#888;font-size:11px;padding:6px 8px;font-family:"Lato",sans-serif}
.hero{left:0;top:157px;width:964px;height:313px;background:var(--brand)}
.hero-kicker{left:92px;top:50px;font-family:"Roboto Condensed",sans-serif;font-size:19px;letter-spacing:2px;color:#fff;border-bottom:1px solid #fff;padding-bottom:1px;width:203px;white-space:nowrap}
.hero-title{left:89px;top:72px;font-family:"Oswald",sans-serif;font-weight:500;font-size:52px;letter-spacing:-2px;color:#fff;border-bottom:1px solid #fff;width:207px;line-height:66px;white-space:nowrap}
.hero-tag{left:499px;top:228px;font-family:"Roboto Condensed",sans-serif;font-size:27px;color:#fff;white-space:nowrap}
.dots{top:484px;height:3px;width:43px;background:#c9c9c9}
.dots.on{background:var(--charcoal)}
.motto{left:0;top:503px;width:964px;text-align:center;font-family:"Roboto Condensed",sans-serif;font-weight:400;font-size:37px;color:var(--ink);text-shadow:1px 2px 2px rgba(0,0,0,.2);letter-spacing:-1px;white-space:nowrap}
.card{top:597px;width:241px;height:328px;background:var(--card);box-shadow:0 2px 0 #dcdcdc}
.card-head{height:42px;background:var(--charcoal);color:#fff;padding:11px 15px}
.card-head.condensed{font-family:"Oswald",sans-serif;font-size:17px;letter-spacing:-.5px}
.card-head.plain{font-family:"Roboto Condensed",sans-serif;font-size:15px;padding-top:13px}
.class-title{font-family:"Roboto Condensed",sans-serif;font-size:11px;color:#222;white-space:nowrap}
.class-title.link{color:var(--link);text-decoration:underline;font-size:12px}
.cal{width:16px;height:18px}
.body-copy{font-size:10.5px;line-height:14.5px;color:var(--muted);font-weight:300}
.more{font-size:8px;color:var(--link);letter-spacing:.3px;white-space:nowrap}
.photo{background:linear-gradient(135deg,#d9d2cc,#a9a09a)}
.rule{height:1px;background:#ddd}
.feature{left:635px;width:241px}
.gold-label{color:#222;font-family:"Roboto Condensed",sans-serif;font-size:14px;white-space:nowrap}
.brand-label{right:6px;color:#fff;font-family:"Roboto Condensed",sans-serif;font-size:14px;white-space:nowrap}
.foot-nav{left:0;top:950px;width:964px;height:40px;background:var(--charcoal)}
.foot-nav a{position:absolute;top:14px;font-family:"Roboto",sans-serif;font-size:9.5px;letter-spacing:.3px;color:#fff;text-decoration:none;white-space:nowrap}
.social{top:13px;width:13px;height:13px;border-radius:50%;background:#fff}
.foot-brand{left:88px;top:1015px;font-family:"Tinos",serif;font-weight:700;font-size:19px;line-height:19px;color:var(--brand)}
.foot-copy{left:88px;top:1068px;width:230px;font-size:8.5px;line-height:14.5px;color:#666;letter-spacing:-.2px}
.foot-addr{left:88px;top:1128px;font-size:8.5px;color:#666;letter-spacing:-.2px;white-space:nowrap}
.foot-head{font-family:"Roboto Condensed",sans-serif;font-size:11.5px;color:#333;white-space:nowrap}
.facilities{left:378px;top:1052px;list-style:none;font-size:9.5px;color:#888;line-height:19.3px}
.facilities li::before{content:"•";margin-right:6px}
.email{left:650px;top:1050px;width:226px;height:27px;background:#fff;border:1px solid #ddd;font-size:9.5px;color:#777;padding:7px 8px}
.join{left:650px;top:1090px;width:97px;height:32px;background:var(--brand);color:#fff;font-family:"Roboto Condensed",sans-serif;font-size:10px;padding:10px 0 0 31px;white-space:nowrap}
.base{left:0;top:1164px;width:964px;height:36px;background:var(--base);border-top:3px solid #3a3a3a;font-family:"Roboto Condensed",sans-serif;font-size:10px;color:#ccc;padding:10px 0 0 119px;white-space:nowrap}
.base b{font-weight:400;color:#fff}
</style>
</head>
<body>

<header class="abs header">
  <div class="abs brand">Plum Harbor Fit</div>
  <div class="abs phone">555 902 6148</div>
  <div class="abs hours">MONDAY - THURSDAY 5:30AM - 10PM<br>FRIDAY 5:30AM - 9PM<br>SATURDAY - SUNDAY 8AM - 6PM</div>
</header>

<nav class="abs nav">
  <a style="left:88px">HOME</a>
  <a style="left:149px">WHO WE ARE</a>
  <a style="left:243px">WHAT WE DO</a>
  <a style="left:330px">WHO WE SERVE</a>
  <a style="left:429px">CONTACT</a>
  <a style="left:508px">BLOG</a>
  <a style="left:570px">MEMBERS</a>
  <div class="abs search">search site</div>
</nav>

<section class="abs hero">
  <svg class="abs" style="left:0;top:0" width="964" height="313">
    <defs>
      <linearGradient id="gymTone" x1="0" y1="0" x2="1" y2="1">
        <stop offset="0" stop-color="#c9cfd4"/>
        <stop offset=".5" stop-color="#8c8a8c"/>
        <stop offset="1" stop-color="#2f3a4a"/>
      </linearGradient>
    </defs>
    <polygon points="574,0 876,0 876,313 261,313" fill="url(#gymTone)" role="img" aria-label="Woman training on a gym machine"/>
    <polygon points="490,220 876,220 876,273 438,273" fill="#323232"/>
  </svg>
  <div class="abs hero-kicker">GET BETTER RESULTS</div>
  <div class="abs hero-title">DR.MARLOWE</div>
  <div class="abs hero-tag">LEARN TO LIVE HEALTHY</div>
</section>

<div class="abs dots on" style="left:687px"></div>
<div class="abs dots" style="left:735px"></div>
<div class="abs dots" style="left:783px"></div>
<div class="abs dots" style="left:832px"></div>

<h1 class="abs motto">I WANT TO LOSE WEIGHT, I WANT TO BE ME.</h1>

<section class="abs card" style="left:88px">
  <div class="card-head condensed">OUR CLASSES</div>
  <svg class="abs cal" style="left:17px;top:56px" viewBox="0 0 16 18"><rect x="0" y="2" width="16" height="16" fill="#ccc"/><rect x="0" y="2" width="16" height="4" fill="#aaa"/><g fill="#fff"><rect x="2" y="8" width="3" height="2"/><rect x="6.5" y="8" width="3" height="2"/><rect x="11" y="8" width="3" height="2"/><rect x="2" y="12" width="3" height="2"/><rect x="6.5" y="12" width="3" height="2"/><rect x="11" y="12" width="3" height="2"/></g></svg>
  <div class="abs class-title" style="left:41px;top:62px">BODY CONTOURING</div>
  <div class="abs photo" style="left:15px;top:89px;width:54px;height:52px" role="img" aria-label="Woman relaxing during a treatment"></div>
  <p class="abs body-copy" style="left:73px;top:88px;width:166px">Duis arcu magna, tristique nec cursus quis, semper non quam. Lorem ipsum dolor sit amet...</p>
  <div class="abs more" style="left:16px;top:164px">MORE DETAILS + TIMES</div>
  <div class="abs rule" style="left:16px;top:179px;width:205px"></div>
  <svg class="abs cal" style="left:17px;top:200px" viewBox="0 0 16 18"><rect x="0" y="2" width="16" height="16" fill="#ccc"/><rect x="0" y="2" width="16" height="4" fill="#aaa"/><g fill="#fff"><rect x="2" y="8" width="3" height="2"/><rect x="6.5" y="8" width="3" height="2"/><rect x="11" y="8" width="3" height="2"/><rect x="2" y="12" width="3" height="2"/><rect x="6.5" y="12" width="3" height="2"/><rect x="11" y="12" width="3" height="2"/></g></svg>
  <div class="abs class-title link" style="left:41px;top:205px">YOGA FOR THE REST OF US</div>
  <p class="abs body-copy" style="left:16px;top:234px;width:210px;font-size:11px;font-family:Arial,sans-serif;color:#777">Duis arcu magna, tristique nec cursus quis, semper non quam. Lorem ipsum dolor sit amet....</p>
  <div class="abs more" style="left:17px;top:289px;text-decoration:underline">MORE DETAILS + TIMES</div>
</section>

<section class="abs card" style="left:361px">
  <div class="card-head plain">ABOUT US</div>
  <div class="abs photo" style="left:17px;top:54px;width:59px;height:59px" role="img" aria-label="Woman lifting weights"></div>
  <p class="abs body-copy" style="left:9px;top:124px;width:230px;color:#666;letter-spacing:-.2px">Welcome to Dr. Lenn Weight Loss Center, where we offer a variety of services to help you look and feel your very best. Our premiere services include SculptWave Body Contouring Treatments, Cavitation, Radio-frequency, &amp; we also offer the safest and most effective medical weight loss program designed specifically for you.</p>
  <div class="abs more" style="left:14px;top:246px">READ MORE</div>
  <div class="abs rule" style="left:9px;top:268px;width:203px"></div>
</section>

<section class="abs feature" style="top:613px;height:136px">
  <svg class="abs" style="left:0;top:0" width="241" height="136">
    <rect width="241" height="98" fill="#a9b6c8" role="img" aria-label="Doctor reviewing a patient chart"/>
    <polygon points="241,20 241,136 133,136" fill="var(--brand)"/>
    <polygon points="0,98 175,98 138,136 0,136" fill="var(--gold)"/>
  </svg>
  <div class="abs gold-label" style="left:12px;top:108px">MEET THE DOCTOR</div>
  <div class="abs brand-label" style="top:108px">DR. MARLOWE</div>
</section>

<section class="abs feature" style="top:771px;height:134px">
  <svg class="abs" style="left:0;top:0" width="241" height="134">
    <rect width="120" height="134" fill="#c4b3a4" role="img" aria-label="Client portrait before treatment"/>
    <rect x="125" width="116" height="134" fill="#c48a6e" role="img" aria-label="Client portrait after treatment"/>
    <polygon points="241,40 241,134 150,134" fill="var(--brand)"/>
    <rect x="0" y="57" width="148" height="37" fill="var(--gold)"/>
  </svg>
  <div class="abs gold-label" style="left:9px;top:68px">SUCCESS STORIES</div>
  <div class="abs brand-label" style="top:113px">DR. MARLOWE</div>
</section>

<nav class="abs foot-nav">
  <a style="left:89px">HOME</a>
  <a style="left:134px">MEDICAL WEIGHT LOSS</a>
  <a style="left:257px">BODY CONTOURING</a>
  <a style="left:365px">BEFORE &amp; AFTER</a>
  <a style="left:459px">REJUVENATION</a>
  <a style="left:543px">CONTACT US</a>
  <a style="left:617px">ESPAÑOL</a>
  <span class="abs social" style="left:733px" aria-label="Social link"></span>
  <span class="abs social" style="left:766px" aria-label="Social link"></span>
  <span class="abs social" style="left:802px" aria-label="Social link"></span>
  <span class="abs social" style="left:834px" aria-label="Social link"></span>
  <span class="abs social" style="left:866px" aria-label="Social link"></span>
</nav>

<div class="abs foot-brand">DR. LENN WEIGHT<br>LOSS CENTER</div>
<p class="abs foot-copy">We provide beneficial treatments using the highest quality products designed to each client's specific needs and total body wellness.</p>
<div class="abs foot-addr">48 Cedar Vale Road Norwick, CT 06100 (555) 014-2290</div>

<div class="abs foot-head" style="left:378px;top:1019px">FACILITIES</div>
<ul class="abs facilities">
  <li>Aquatic</li>
  <li>Beauty treatments</li>
  <li>Weight training</li>
  <li>Cardio workouts</li>
</ul>

<div class="abs foot-head" style="left:650px;top:1019px">FREE FITNESS NEWSLETTER</div>
<div class="abs email">Your Email Address</div>
<div class="abs join">JOIN TODAY
  <svg class="abs" style="left:9px;top:9px" width="17" height="14" viewBox="0 0 17 14"><polygon points="0,7 17,0 12,14 8,9" fill="#fff"/><polygon points="8,9 17,0 6,13" fill="#e6dcef"/></svg>
</div>

<footer class="abs base">Copyright 2014 All Right Reserved Plum Harbor Fit . &nbsp;&nbsp; Designed by: &nbsp;<b>Brightfold Studio</b></footer>

</body>
</html>
```